Lantern Vale Photography business card design required

Needing business card made up for my new photography business.

Target Market(s)

Target will mostly be regular people with the occasional industrial or commercial customer.

Industry/Entity Type

Business

Font styles to use
Sans Serif

Colors

Designer to choose colors to be used in the design.

Requirements
Must have
• Morgan Tillbrook
Ph: 0437 262 508
Email: info@lanternvalephoto.example
Web: www.lanternvalephoto.example

On the back possibly links for social media including Townsquare, Lensroll and Shutterfeed (links to be determined).

```html
<!DOCTYPE html>
<html lang="en">
<head>
<meta charset="utf-8">
<title>Lantern Vale Photography – Business Card</title>
<link rel="stylesheet" href="https://fonts.googleapis.com/css2?family=Arimo:wght@400;700&display=swap">
<style>
  :root {
    --backdrop: #f1f1f1;
    --card-light: #ffffff;
    --card-dark: #343434;
    --accent-blue: #2a8fd0;
    --ink-dark: #3a3a3a;
    --ink-body: #2c2c2c;
    --ink-light: #c9c9c9;
  }
  * { margin: 0; padding: 0; box-sizing: border-box; }
  html, body {
    width: 1200px; height: 908px; overflow: hidden;
    background: var(--backdrop);
    font-family: "Arimo", Arial, sans-serif;
  }
  .canvas { position: relative; width: 1200px; height: 908px; }

  .card { position: absolute; overflow: hidden; box-shadow: 0 2px 6px rgba(0,0,0,0.12); }
  .card svg.card-lines { position: absolute; inset: 0; }

  /* Front */
  .card-front { left: 145px; top: 300px; width: 540px; height: 309px; background: var(--card-light); }
  .front-brand {
    position: absolute; left: 135px; top: 140px; width: 160px;
    font-weight: 700; font-size: 15px; line-height: 20px; letter-spacing: 0.5px;
    color: var(--ink-dark); text-align: center;
  }
  .holder-name {
    position: absolute; left: 268px; top: 84px;
    font-weight: 700; font-size: 22px; letter-spacing: 0.3px; color: var(--ink-dark);
  }
  .holder-name .first { color: var(--accent-blue); }
  .contact-phone {
    position: absolute; right: 25px; top: 118px;
    font-size: 11px; line-height: 15px; text-align: right; color: var(--ink-body);
  }
  .contact-list {
    position: absolute; left: 280px; top: 146px;
    font-size: 11px; line-height: 15.5px; color: var(--ink-body); list-style: none;
  }

  /* Back */
  .card-back { left: 746px; top: 184px; width: 309px; height: 540px; background: var(--card-dark); }
  .back-brand {
    position: absolute; left: 0; top: 248px; width: 100%; text-align: center;
    font-weight: 700; font-size: 17px; line-height: 24px; letter-spacing: 1px; color: var(--ink-light);
  }
</style>
</head>
<body>
<main class="canvas">

  <section class="card card-front" aria-label="Business card front">
    <svg class="card-lines" width="540" height="309" viewBox="0 0 540 309" aria-hidden="true">
      <line x1="215" y1="0" x2="215" y2="118" stroke="var(--accent-blue)" stroke-width="2"/>
      <line x1="215" y1="200" x2="215" y2="309" stroke="var(--accent-blue)" stroke-width="2"/>
      <line x1="265" y1="110" x2="540" y2="110" stroke="var(--accent-blue)" stroke-width="2"/>
    </svg>
    <p class="front-brand">LANTERN VALE<br>PHOTOGRAPHY</p>
    <h1 class="holder-name"><span class="first">MORGAN</span> TILLBROOK</h1>
    <p class="contact-phone">0437 262 508</p>
    <ul class="contact-list">
      <li>info@lanternvalephoto.example</li>
      <li>www.lanternvalephoto.example</li>
      <li>Townsquare</li>
      <li>Lensroll</li>
      <li>Shutterfeed</li>
    </ul>
  </section>

  <section class="card card-back" aria-label="Business card back">
    <svg class="card-lines" width="309" height="540" viewBox="0 0 309 540" aria-hidden="true">
      <line x1="155" y1="0" x2="155" y2="225" stroke="var(--accent-blue)" stroke-width="2"/>
      <line x1="155" y1="315" x2="155" y2="540" stroke="var(--accent-blue)" stroke-width="2"/>
      <line x1="0" y1="370" x2="26" y2="370" stroke="var(--accent-blue)" stroke-width="2"/>
      <line x1="283" y1="172" x2="309" y2="172" stroke="var(--accent-blue)" stroke-width="2"/>
    </svg>
    <p class="back-brand">LANTERN VALE<br>PHOTOGRAPHY</p>
  </section>

</main>
</body>
</html>
```